Business Card Design Project

Financial planning, Insurance and Real estate - Financial Services company

Contact Information for Business Card

Looking for something simple in design -
Tolverin Equity LLC
Tolverin Wealth Managment

```html
<!DOCTYPE html>
<html lang="en">
<head>
<meta charset="utf-8">
<title>Tolverin Wealth Management – Business Card</title>
<link rel="stylesheet" href="https://fonts.googleapis.com/css2?family=Lato:wght@400;700&display=swap">
<style>
  :root {
    --page-bg: #e9e9e9;
    --card-bg: #f6f6f6;
    --brand-blue: #0b7cc1;
    --ink: #1c1c1c;
    --charcoal: #3b3b3b;
    --white: #ffffff;
  }
  * { margin: 0; padding: 0; box-sizing: border-box; }
  html, body {
    width: 1200px;
    height: 985px;
    overflow: hidden;
    background: var(--page-bg);
    font-family: "Lato", Arial, sans-serif;
  }
  .card {
    position: absolute;
    left: 100px;
    top: 192px;
    width: 1000px;
    height: 600px;
    background: var(--card-bg);
    overflow: hidden;
  }
  .identity {
    position: absolute;
    left: 78px;
    top: 76px;
  }
  .person-name {
    font-size: 25px;
    font-weight: 400;
    color: var(--brand-blue);
    line-height: 1.2;
  }
  .person-name strong { font-weight: 700; }
  .person-title {
    font-size: 19px;
    color: var(--ink);
    margin-top: 4px;
  }
  .website {
    font-size: 21px;
    font-weight: 700;
    color: var(--brand-blue);
    margin-top: 26px;
  }
  .company-name {
    position: absolute;
    left: 568px;
    top: 322px;
    width: 340px;
    text-align: center;
    font-size: 25px;
    font-weight: 700;
    color: var(--brand-blue);
  }
  .contact-tab {
    position: absolute;
    left: 0;
    top: 362px;
    width: 69px;
    height: 150px;
    background: var(--brand-blue);
    border-radius: 0 16px 16px 0;
  }
  .contact-tab svg {
    position: absolute;
    left: 23px;
    width: 22px;
    height: 22px;
  }
  .contact-list {
    position: absolute;
    left: 91px;
    top: 376px;
    list-style: none;
  }
  .contact-list li {
    font-size: 22px;
    color: var(--ink);
    height: 45px;
    line-height: 32px;
  }
  .footer-bands {
    position: absolute;
    left: 0;
    bottom: 0;
    width: 1000px;
    height: 32px;
  }
</style>
</head>
<body>
  <main class="card">
    <div class="identity">
      <h1 class="person-name">Marissa <strong>Holloway</strong></h1>
      <p class="person-title">Chief Executive Offer</p>
      <p class="website">www.tolverinwealthm.com</p>
    </div>

    <p class="company-name">Tolverin Wealth Management</p>

    <div class="contact-tab">
      <svg style="top:19px" viewBox="0 0 24 24" aria-label="Phone">
        <path fill="#fff" d="M3 7c0-2 3-4 9-4s9 2 9 4v2h-5V7.5c-1-.6-2.5-.9-4-.9s-3 .3-4 .9V9H3z M6 11h12l2 8H4z"/>
        <circle cx="12" cy="15" r="2" fill="#0b7cc1"/>
      </svg>
      <svg style="top:64px" viewBox="0 0 24 24" aria-label="Email">
        <rect x="2" y="5" width="20" height="14" fill="none" stroke="#fff" stroke-width="2"/>
        <path d="M2 5l10 8 10-8" fill="none" stroke="#fff" stroke-width="2"/>
      </svg>
      <svg style="top:108px" viewBox="0 0 24 24" aria-label="Location">
        <path fill="#fff" d="M12 2a7 7 0 0 0-7 7c0 5 7 13 7 13s7-8 7-13a7 7 0 0 0-7-7z"/>
        <circle cx="12" cy="9" r="2.6" fill="#0b7cc1"/>
      </svg>
    </div>

    <ul class="contact-list">
      <li>919.555.0148</li>
      <li>mholloway@brightlanemail.com</li>
      <li>4815 Harbor Pointe Dr, Suite 210, Cary, NC 27513</li>
    </ul>

    <svg class="footer-bands" viewBox="0 0 1000 32" preserveAspectRatio="none">
      <rect x="0" y="8" width="1000" height="24" fill="var(--charcoal)"/>
      <path d="M592 32 Q600 2 632 2 H1000 V32 Z" fill="var(--white)"/>
      <path d="M602 32 Q610 8 640 8 H1000 V32 Z" fill="var(--brand-blue)"/>
    </svg>
  </main>
</body>
</html>
```